The amber lantern with an elephant incorporated in the background

Target Market(s)

Real estate

Industry/Entity Type

Real Estate

Contact Information for Business Card

On back on want my name & number
In front I want the business name, "the amber lantern", below to say staging & design

Logo Text

The amber lantern

Font styles to use
Serif

Colors
000000

Requirements
Must have
• I want an elephant behind the writing in gold transperant

```html
<!DOCTYPE html>
<html lang="en">
<head>
<meta charset="utf-8">
<title>The Amber Lantern – Business Cards</title>
<link rel="stylesheet" href="https://fonts.googleapis.com/css2?family=Cinzel:wght@600&family=Cormorant+Garamond:wght@400;500&display=swap">
<style>
  :root {
    --backdrop: #2b2b2b;
    --card-dark: #3a3a3a;
    --card-dark-edge: #2f2f2f;
    --card-light: #f4f4f4;
    --card-light-edge: #e2e2e2;
    --ink-dark: #3d3d3d;
    --ink-light: #e9e9e9;
    --ink-muted: #cfcfcf;
    --rule: #d8d8d8;
    --gold-high: #f3d36b;
    --gold-mid: #c9962a;
    --gold-low: #7a5a12;
  }
  html, body {
    margin: 0;
    width: 1200px;
    height: 997px;
    overflow: hidden;
    background: var(--backdrop);
  }
  .canvas {
    position: relative;
    width: 1200px;
    height: 997px;
  }
  .card {
    position: absolute;
    left: 300px;
    width: 600px;
    height: 340px;
    border-radius: 22px;
    overflow: hidden;
    box-shadow: 0 14px 30px rgba(0,0,0,.45);
  }

  /* Back of card */
  .card--back {
    top: 125px;
    background: linear-gradient(160deg, var(--card-dark) 0%, var(--card-dark-edge) 100%);
    color: var(--ink-light);
  }
  .holder-name {
    position: absolute;
    top: 62px;
    width: 100%;
    text-align: center;
    margin: 0;
    font-family: "Cinzel", serif;
    font-weight: 600;
    font-size: 26px;
    letter-spacing: 1px;
    color: var(--ink-light);
  }
  .holder-role {
    position: absolute;
    top: 104px;
    width: 100%;
    text-align: center;
    margin: 0;
    font-family: "Cormorant Garamond", serif;
    font-size: 17px;
    letter-spacing: 7px;
    color: var(--ink-muted);
  }
  .rule {
    position: absolute;
    left: 40px;
    right: 40px;
    height: 2px;
    background: var(--rule);
  }
  .rule--top { top: 150px; }
  .rule--bottom { top: 262px; }
  .contact-line {
    position: absolute;
    top: 188px;
    width: 100%;
    display: flex;
    justify-content: center;
    align-items: center;
    gap: 12px;
    font-family: "Cormorant Garamond", serif;
    font-size: 19px;
    color: var(--ink-light);
  }
  .contact-line .icon {
    width: 30px;
    height: 30px;
  }
  .elephant-mark {
    position: absolute;
    left: 40px;
    top: 274px;
    width: 76px;
    height: 54px;
    border-radius: 40% 45% 30% 30%;
    background: radial-gradient(ellipse at 55% 40%, var(--gold-mid) 0%, var(--gold-low) 70%, transparent 100%);
    opacity: .55;
  }

  /* Front of card */
  .card--front {
    top: 525px;
    background: linear-gradient(160deg, #ffffff 0%, var(--card-light) 55%, var(--card-light-edge) 100%);
    color: var(--ink-dark);
  }
  .business-name {
    position: absolute;
    top: 42px;
    right: 50px;
    margin: 0;
    font-family: "Cormorant Garamond", serif;
    font-weight: 500;
    font-size: 32px;
    letter-spacing: 1px;
    text-transform: uppercase;
    color: var(--ink-dark);
  }
  .business-tagline {
    position: absolute;
    top: 88px;
    right: 50px;
    margin: 0;
    font-family: "Cormorant Garamond", serif;
    font-size: 17px;
    letter-spacing: 9px;
    text-transform: uppercase;
    color: var(--ink-dark);
  }
  .elephant-figure {
    position: absolute;
    left: 190px;
    top: 132px;
    width: 260px;
    height: 180px;
    border-radius: 42% 48% 30% 32%;
    background: radial-gradient(ellipse at 50% 40%, var(--gold-high) 0%, var(--gold-mid) 50%, var(--gold-low) 85%, transparent 100%);
  }
</style>
</head>
<body>
<main class="canvas">
  <section class="card card--back" aria-label="Card back">
    <h2 class="holder-name">MARTIN OAKES</h2>
    <p class="holder-role">Property Consultant</p>
    <div class="rule rule--top"></div>
    <div class="contact-line">
      <svg class="icon" viewBox="0 0 30 30" aria-hidden="true">
        <circle cx="15" cy="15" r="14" fill="#e9e9e9"/>
        <rect x="10.5" y="7" width="9" height="16" rx="1.8" fill="none" stroke="#3a3a3a" stroke-width="1.6"/>
        <circle cx="15" cy="20.5" r="0.9" fill="#3a3a3a"/>
      </svg>
      <span class="phone">07700 900417</span>
    </div>
    <div class="rule rule--bottom"></div>
    <div class="elephant-mark" role="img" aria-label="Small gold elephant figure"></div>
  </section>

  <section class="card card--front" aria-label="Card front">
    <h1 class="business-name">The Amber Lantern</h1>
    <p class="business-tagline">Staging &amp; Design</p>
    <div class="elephant-figure" role="img" aria-label="Gold elephant figure with raised trunk"></div>
  </section>
</main>
</body>
</html>
```